Design für 3-Monatskalender
Zielgruppe
Hallo, wir benötigen ein Design bzw. fertige Druckdaten für einen 3 Monatskalender mit den Feiertagen aus DE, AT und CH.
Format ist DIN A6, der Kalender wird benötigt für das Jahr 2024 und 2025.
Aufgabenstellung
Format: DIN A6
Kalendarium 2024 und 2025
Feiertage aus DE, AT und CH
Beispiel anbei, wichtig ist, das wir einen Magnetischen Ring als Datumsschieber nehmen. Der Ring hat die Maße: Durchmesser = 12mm Innendruchmesser = 10mm

```html
<!DOCTYPE html>
<html lang="de">
<head>
<meta charset="utf-8">
<title>3-Monatskalender 2024</title>
<link href="https://fonts.googleapis.com/css2?family=Barlow:wght@300;400;700&display=swap" rel="stylesheet">
<style>
:root{
  --page:#ececec;
  --panel-grey:#dadada;
  --panel-white:#ffffff;
  --ink:#1c1c1c;
  --rule:#8c8c8c;
  --holiday:#b3141c;
}
*{margin:0;padding:0;box-sizing:border-box}
html,body{width:849px;height:1200px;overflow:hidden;background:var(--page)}
body{font-family:"Barlow",Arial,sans-serif;color:var(--ink);position:relative}
.calendar{position:absolute;left:72px;top:75px;width:384px;box-shadow:3px 4px 6px rgba(0,0,0,.18)}
.month{position:relative;padding-left:20px;background:var(--panel-grey);font-weight:300}
.month--current{background:var(--panel-white);font-weight:700}
.month--dec{height:192px;padding-top:18.6px}
.month--jan{height:181px;padding-top:8px}
.month--feb{height:187px;padding-top:8.7px}
.month-title{height:16px;display:flex;align-items:center;font-size:14px;line-height:16px}
.month-title .year{width:58.6px}
.month-title .bar{margin:0 6px}
.grid{display:grid;grid-template-columns:36px repeat(7,44.5px);width:347.5px}
.labels{height:16px;margin-top:4px;margin-bottom:3.2px;font-size:4.6px;line-height:5.2px;font-weight:400}
.labels span{text-align:center;padding-left:10px}
.labels .wk-label{text-align:right;padding:0 8px 0 0}
.row{height:25.6px;align-items:center;font-size:19px}
.row+.row{border-top:1px solid var(--rule)}
.row span{text-align:right;line-height:25px;white-space:nowrap}
.row .wk{font-size:13px;font-weight:300;padding-right:8px}
.row .sun{color:var(--holiday)}
.mark{display:inline-block;width:5px;height:12px;vertical-align:middle;margin:0 1px}
</style>
</head>
<body>
<main class="calendar">

<section class="month month--dec">
  <h2 class="month-title"><span class="year">2023</span>Dezember<span class="bar">|</span>December<span class="bar">|</span>Décembre</h2>
  <div class="grid labels"><span class="wk-label">Woche<br>Week<br>Semaine</span><span>Montag<br>Monday<br>Lundi</span><span>Dienstag<br>Tuesday<br>Mardi</span><span>Mittwoch<br>Wednesday<br>Mercredi</span><span>Donnerstag<br>Thursday<br>Jeudi</span><span>Freitag<br>Friday<br>Vendreday</span><span>Samstag<br>Saturday<br>Samedi</span><span>Sonntag<br>Sunday<br>Dimanche</span></div>
  <div class="grid row"><span class="wk">48</span><span></span><span></span><span></span><span></span><span>1</span><span>2</span><span class="sun">3</span></div>
  <div class="grid row"><span class="wk">49</span><span>4</span><span>5</span><span>6</span><span>7</span><span><svg class="mark" viewBox="0 0 5 12"><circle cx="2.5" cy="3" r="1.8" fill="none" stroke="#b3141c" stroke-width=".8"/><circle cx="2.5" cy="7" r="1.8" fill="none" stroke="#b3141c" stroke-width=".8"/></svg>8</span><span>9</span><span class="sun">10</span></div>
  <div class="grid row"><span class="wk">50</span><span>11</span><span>12</span><span>13</span><span>14</span><span>15</span><span>16</span><span class="sun">17</span></div>
  <div class="grid row"><span class="wk">51</span><span>18</span><span>19</span><span>20</span><span>21</span><span>22</span><span>23</span><span class="sun">24</span></div>
  <div class="grid row"><span class="wk">52</span><span>25<svg class="mark" viewBox="0 0 5 12"><circle cx="2.5" cy="2" r="1.6" fill="none" stroke="#b3141c" stroke-width=".8"/><circle cx="2.5" cy="6" r="1.6" fill="none" stroke="#b3141c" stroke-width=".8"/><circle cx="2.5" cy="10" r="1.6" fill="none" stroke="#b3141c" stroke-width=".8"/></svg></span><span>26<svg class="mark" viewBox="0 0 5 12"><circle cx="2.5" cy="2" r="1.6" fill="none" stroke="#b3141c" stroke-width=".8"/><circle cx="2.5" cy="6" r="1.6" fill="none" stroke="#b3141c" stroke-width=".8"/><circle cx="2.5" cy="10" r="1.6" fill="none" stroke="#b3141c" stroke-width=".8"/></svg></span><span>27</span><span>28</span><span>29</span><span>30</span><span class="sun">31</span></div>
</section>

<section class="month month--current month--jan">
  <h2 class="month-title"><span class="year">2024</span>Januar<span class="bar">|</span>January<span class="bar">|</span>Janvier</h2>
  <div class="grid labels"><span class="wk-label">Woche<br>Week<br>Semaine</span><span>Montag<br>Monday<br>Lundi</span><span>Dienstag<br>Tuesday<br>Mardi</span><span>Mittwoch<br>Wednesday<br>Mercredi</span><span>Donnerstag<br>Thursday<br>Jeudi</span><span>Freitag<br>Friday<br>Vendreday</span><span>Samstag<br>Saturday<br>Samedi</span><span>Sonntag<br>Sunday<br>Dimanche</span></div>
  <div class="grid row"><span class="wk">1</span><span><svg class="mark" viewBox="0 0 5 12"><circle cx="2.5" cy="2" r="1.6" fill="none" stroke="#b3141c" stroke-width=".8"/><circle cx="2.5" cy="6" r="1.6" fill="none" stroke="#b3141c" stroke-width=".8"/><circle cx="2.5" cy="10" r="1.6" fill="none" stroke="#b3141c" stroke-width=".8"/></svg>1</span><span>2</span><span>3</span><span>4</span><span>5</span><span><svg class="mark" viewBox="0 0 5 12"><circle cx="2.5" cy="3" r="1.8" fill="none" stroke="#b3141c" stroke-width=".8"/><circle cx="2.5" cy="7" r="1.8" fill="none" stroke="#b3141c" stroke-width=".8"/></svg>6</span><span class="sun">7</span></div>
  <div class="grid row"><span class="wk">2</span><span>8</span><span>9</span><span>10</span><span>11</span><span>12</span><span>13</span><span class="sun">14</span></div>
  <div class="grid row"><span class="wk">3</span><span>15</span><span>16</span><span>17</span><span>18</span><span>19</span><span>20</span><span class="sun">21</span></div>
  <div class="grid row"><span class="wk">4</span><span>22</span><span>23</span><span>24</span><span>25</span><span>26</span><span>27</span><span class="sun">28</span></div>
  <div class="grid row"><span class="wk">5</span><span>29</span><span>30</span><span>31</span><span></span><span></span><span></span><span></span></div>
</section>

<section class="month month--feb">
  <h2 class="month-title"><span class="year">2024</span>Februar<span class="bar">|</span>February<span class="bar">|</span>Février</h2>
  <div class="grid labels"><span class="wk-label">Woche<br>Week<br>Semaine</span><span>Montag<br>Monday<br>Lundi</span><span>Dienstag<br>Tuesday<br>Mardi</span><span>Mittwoch<br>Wednesday<br>Mercredi</span><span>Donnerstag<br>Thursday<br>Jeudi</span><span>Freitag<br>Friday<br>Vendreday</span><span>Samstag<br>Saturday<br>Samedi</span><span>Sonntag<br>Sunday<br>Dimanche</span></div>
  <div class="grid row"><span class="wk">5</span><span></span><span></span><span></span><span>1</span><span>2</span><span>3</span><span class="sun">4</span></div>
  <div class="grid row"><span class="wk">6</span><span>5</span><span>6</span><span>7</span><span>8</span><span>9</span><span>10</span><span class="sun">11</span></div>
  <div class="grid row"><span class="wk">7</span><span>12</span><span>13</span><span>14</span><span>15</span><span>16</span><span>17</span><span class="sun">18</span></div>
  <div class="grid row"><span class="wk">8</span><span>19</span><span>20</span><span>21</span><span>22</span><span>23</span><span>24</span><span class="sun">25</span></div>
  <div class="grid row"><span class="wk">9</span><span>26</span><span>27</span><span>28</span><span>29</span><span></span><span></span><span></span></div>
</section>

</main>
</body>
</html>
```